IT Professional business card with a hometown feel and a little edgy.

My business name is Tamble Website Solutions. But I have ended up doing much more. I live in a very small remote community, where everyone knows everyone. We like the one-on-one customer service in this community. I do computer tutoring, virus removal, networking, and software training. My clients are businesses and private individuals.

My website is tamblewebsitesolutions.example, when I first designed it I was going for a fresh, clean look, which I still like. But I am thinking about making the website a bit more edgy to match my new logo from ArtHively (logo attached). At this time my website does not display the new logo, but I plan on redesigning the website in the future to match the logo and business card.

My tag line is "put the web to work for you"

I'm thinking I would like to have the business card printed with a metallic finish.
Updates

Please do not use black backgrounds, or any solid dark colors. Prefer light or white backgrounds.

Target Market(s)

Small businesses. Individuals that need computer help at home.

Industry/Entity Type

It Company

Contact Information for Business Card

Nora Prandell
Tamble Website Solutions
PO Box 7153
Ridgeholm, WA 98417
Cell: 555-271-3096
nora@tamblewebsitesolutions.example
tamblewebsitesolutions.example

Font styles to use
Serif

Requirements
Must have
• Must have all the information listed in "Business Card Details"
• Must use the logo provided.
• Use the colors from the provided logo
Nice to have
• Would like to use my tagline "put the web to work for you" all lowercase

```html
<!DOCTYPE html>
<html lang="en">
<head>
<meta charset="utf-8">
<title>Tamble Website Solutions – Business Card</title>
<link rel="stylesheet" href="https://fonts.googleapis.com/css2?family=Open+Sans:wght@400;600&display=swap">
<style>
  :root {
    --green: #3c7a2e;
    --green-dark: #25611d;
    --green-light: #5d9a45;
    --grey-text: #4a4a4a;
    --dark-text: #2e2e2e;
    --card: #ffffff;
    --stage: #ecebe8;
  }
  * { box-sizing: border-box; margin: 0; padding: 0; }
  html, body { width: 1200px; height: 837px; overflow: hidden; }
  body {
    background: var(--stage);
    font-family: "Open Sans", sans-serif;
    position: relative;
  }
  .card {
    position: absolute;
    top: 262px;
    width: 520px;
    height: 312px;
    background: var(--card);
    border-radius: 22px;
    overflow: hidden;
    box-shadow: 0 6px 18px rgba(0,0,0,.18);
  }
  .card__band {
    position: absolute;
    left: 0; right: 0; bottom: 0;
    height: 22px;
    background: linear-gradient(180deg, var(--green-light), var(--green-dark));
  }

  /* Contact side */
  .card--contact { left: 50px; }
  .contact__company {
    position: absolute;
    left: 34px; top: 28px;
    font-size: 33px;
    font-weight: 400;
    color: var(--grey-text);
    letter-spacing: -0.3px;
    white-space: nowrap;
  }
  .contact__company-lead { color: var(--green); }
  .contact__person {
    position: absolute;
    left: 34px; top: 80px;
    font-size: 19px;
    color: var(--grey-text);
  }
  .contact__list {
    position: absolute;
    left: 0; top: 128px;
    list-style: none;
  }
  .contact__row {
    display: flex;
    align-items: center;
    height: 24px;
    margin-bottom: 10px;
  }
  .contact__tab {
    width: 52px;
    height: 20px;
    background: linear-gradient(90deg, var(--green-dark), var(--green-light));
    display: flex;
    align-items: center;
    justify-content: flex-end;
    padding-right: 8px;
    margin-right: 10px;
  }
  .contact__tab svg { width: 13px; height: 13px; fill: #fff; }
  .contact__text { font-size: 16px; color: var(--dark-text); white-space: nowrap; }

  /* Brand side */
  .card--brand { left: 630px; }
  .brand__name {
    position: absolute;
    left: 0; right: 0; top: 58px;
    display: flex;
    align-items: center;
    justify-content: center;
    gap: 18px;
  }
  .brand__square {
    width: 34px; height: 34px;
    background: var(--green);
  }
  .brand__text {
    font-size: 27px;
    font-weight: 400;
    line-height: 1.05;
    color: var(--green);
  }
  .brand__tagline {
    position: absolute;
    left: 0; right: 0; top: 196px;
    text-align: center;
    font-size: 25px;
    color: var(--grey-text);
    white-space: nowrap;
  }
</style>
</head>
<body>

<section class="card card--contact" aria-label="Contact side">
  <h1 class="contact__company"><span class="contact__company-lead">Tamble</span> Website Solutions</h1>
  <p class="contact__person">Nora Prandell</p>
  <ul class="contact__list">
    <li class="contact__row">
      <span class="contact__tab"><svg viewBox="0 0 16 16" aria-hidden="true"><path d="M3 1h3l1.5 4-2 1.2a9 9 0 0 0 4.3 4.3L11 8.5l4 1.5v3a2 2 0 0 1-2 2A12 12 0 0 1 1 3a2 2 0 0 1 2-2z"/></svg></span>
      <span class="contact__text">555-271-3096</span>
    </li>
    <li class="contact__row">
      <span class="contact__tab"><svg viewBox="0 0 16 16" aria-hidden="true"><path d="M8 0a5.5 5.5 0 0 1 5.5 5.5C13.5 10 8 16 8 16S2.5 10 2.5 5.5A5.5 5.5 0 0 1 8 0zm0 3.3a2.2 2.2 0 1 0 0 4.4 2.2 2.2 0 0 0 0-4.4z"/></svg></span>
      <span class="contact__text">PO Box 7153, Ridgeholm, WA 98417</span>
    </li>
    <li class="contact__row">
      <span class="contact__tab"><svg viewBox="0 0 16 16" aria-hidden="true"><path d="M1 3h14v10H1zM2 4.2v.6l6 4 6-4v-.6z" fill-rule="evenodd"/></svg></span>
      <span class="contact__text">nora@tamblewebsitesolutions.example</span>
    </li>
    <li class="contact__row">
      <span class="contact__tab"><svg viewBox="0 0 16 16" aria-hidden="true"><path d="M8 1a7 7 0 1 0 0 14A7 7 0 0 0 8 1zm0 1.3c.8.9 1.4 2.2 1.6 3.7H6.4C6.6 4.5 7.2 3.2 8 2.3zM2.4 7.3h2.7a10 10 0 0 0 0 1.4H2.4a5.7 5.7 0 0 1 0-1.4zm4 0h3.2a9 9 0 0 1 0 1.4H6.4a9 9 0 0 1 0-1.4zm4.5 0h2.7a5.7 5.7 0 0 1 0 1.4h-2.7a10 10 0 0 0 0-1.4zM6.4 10h3.2c-.2 1.5-.8 2.8-1.6 3.7-.8-.9-1.4-2.2-1.6-3.7z"/></svg></span>
      <span class="contact__text">tamblewebsitesolutions.example</span>
    </li>
  </ul>
  <div class="card__band"></div>
</section>

<section class="card card--brand" aria-label="Brand side">
  <div class="brand__name">
    <span class="brand__square"></span>
    <span class="brand__text">Tamble<br>Website<br>Solutions</span>
  </div>
  <p class="brand__tagline">put the web to work for you</p>
  <div class="card__band"></div>
</section>

</body>
</html>
```